Protrait photographers business card

Need a new catchy, chic business card to promote my new portrait photograghy business. Love taking the natural, location portraits of families, children, teens. It should look classy, but also warm & friendly. I want it to show that Famliy, friends, couples & childten are what I love photographing, so if it can have that sort of feel to it & also looking energetic.

Target Market(s)

Families, couples, babies, people on holidays wanting some locational professional photos

Industry/Entity Type

Portrait Photography

Contact Information for Business Card

Lumivale photography, By Tavi, Norah Balfrey,Ph: 0487356024, Kestrel cove, Qld

Font styles to use
Decorative
Script

Requirements
Must have
• Company name & photographers name
Nice to have
• a coloured card
Should not have
• not be on a white card

```html
<!DOCTYPE html>
<html lang="en">
<head>
<meta charset="utf-8">
<title>Lumivale photography – business card</title>
<link rel="stylesheet" href="https://fonts.googleapis.com/css2?family=Poiret+One&display=swap">
<style>
  :root {
    --stone-dark: #161616;
    --stone-mid: #3a3a3a;
    --stone-light: #555555;
    --portrait-dark: #101010;
    --portrait-light: #9a9a9a;
    --accent-yellow: #f5e81c;
    --text-light: #ffffff;
    --text-dark: #0d0d0d;
  }
  html, body {
    margin: 0;
    padding: 0;
    overflow: hidden;
    background: #202020;
  }
  .card {
    position: relative;
    width: 1200px;
    height: 741px;
    overflow: hidden;
    font-family: "Poiret One", "Century Gothic", sans-serif;
  }
  .stone-backdrop {
    position: absolute;
    inset: 0;
    background:
      radial-gradient(ellipse at 60% 40%, var(--stone-light) 0%, var(--stone-mid) 45%, var(--stone-dark) 100%);
  }
  .portrait-area {
    position: absolute;
    left: 0;
    top: 150px;
    width: 470px;
    height: 591px;
    background: linear-gradient(160deg, var(--portrait-light) 0%, #5a5a5a 35%, var(--portrait-dark) 80%);
    border-radius: 48% 52% 0 0 / 30% 30% 0 0;
    opacity: 0.85;
  }
  .photographer-details {
    position: absolute;
    left: 673px;
    top: 38px;
    margin: 0;
    color: var(--text-light);
    font-size: 50px;
    line-height: 76px;
    letter-spacing: 1px;
  }
  .photographer-details p { margin: 0; }
  .contact-band {
    position: absolute;
    left: 580px;
    top: 365px;
    right: 0;
    height: 162px;
    background: var(--accent-yellow);
    border-radius: 81px 0 0 81px;
  }
  .contact-list {
    position: absolute;
    left: 90px;
    top: 14px;
    margin: 0;
    padding: 0;
    list-style: none;
    color: var(--text-dark);
    font-size: 37px;
    line-height: 48px;
  }
  .contact-list li {
    display: flex;
    align-items: center;
    gap: 10px;
  }
  .contact-icon {
    width: 36px;
    height: 36px;
    flex: none;
  }
  .social-dot {
    width: 22px;
    height: 22px;
    margin: 0 7px;
    border-radius: 50%;
    background: var(--text-dark);
    flex: none;
  }
  .studio-name {
    position: absolute;
    left: 54px;
    top: 540px;
    margin: 0;
    color: var(--accent-yellow);
    font-size: 66px;
    line-height: 72px;
    font-weight: 400;
  }
  .studio-name span { display: block; }
</style>
</head>
<body>
  <main class="card">
    <div class="stone-backdrop" role="img" aria-label="Dark black and white stone wall texture"></div>
    <div class="portrait-area" role="img" aria-label="Black and white portrait of a woman with long hair looking over her shoulder"></div>

    <section class="photographer-details">
      <p class="person-name">Norah Balfrey</p>
      <p class="phone">0487356024</p>
      <p class="locality">Kestrel Cove,</p>
      <p class="state">Queensland</p>
    </section>

    <section class="contact-band">
      <ul class="contact-list">
        <li>
          <svg class="contact-icon" viewBox="0 0 36 36" aria-hidden="true">
            <rect x="2" y="8" width="32" height="21" fill="var(--text-dark)"/>
            <polyline points="3,9 18,21 33,9" fill="none" stroke="var(--accent-yellow)" stroke-width="2"/>
          </svg>
          <span>info@lumivale.com</span>
        </li>
        <li><span class="social-dot"></span><span>lumivale.net/tavi123</span></li>
        <li><span class="social-dot"></span><span>feedline.net/tavi123</span></li>
      </ul>
    </section>

    <h1 class="studio-name">
      <span>Lumivale photography</span>
      <span>By Tavi</span>
    </h1>
  </main>
</body>
</html>
```